Sports Nutrition Product that needs a label

We are seeking an editable label design for our company Vel OrtaWorks. We are looking for a creative, yet clean design. Front of label should include the following information: our logo, Premium Full Spectrum Hemp Extract, 1,200mg, lemon zest, and 0.5 fl oz 15ml. Under our logo in matching blue font we would like to add the following phrase: balanced mind. balanced body. balanced life. Back of label to include Supplemental Facts table (see uploaded example, we will need to be able to change the numbers). Other information that should be included on the back of label: Ingredients: Whole hemp plant extract, organic cold-pressed hemp seed oil, terpenes. *Contains <0.3% THC
Suggested Use: Shake well before using. Store in a cool, dry place away from light. Do not use if seal is broken.
Adults: Take 1 dropper full (approx. 1ml) up to 3 times daily, held under the tongue for 60 seconds before ingesting.
If pregnant or nursing do not use this product. If you have a serious medical condition or take pharmaceutical drugs, consult your doctor prior to use. Keep out of reach of children.
Hemp grown proudly in the USA

We will also need a place to put a QR code and UPC code.

Please note the files titled front example and supplement table ex are only ideas of overall design we like and are not to be copied.

```html
<!DOCTYPE html>
<html lang="en">
<head>
<meta charset="utf-8">
<title>Vel OrtaWorks Premium Hemp Extract Label</title>
<link href="https://fonts.googleapis.com/css2?family=Saira:wght@400;500;600&display=swap" rel="stylesheet">
<style>
  :root {
    --backdrop: #7a7a7a;
    --label-black: #1a1a1c;
    --band-blue: #1aa3e0;
    --band-cyan: #20d0f5;
    --band-deep: #0a5fa8;
    --brand-green: #5cb646;
    --chip-green: #8cc63f;
    --zest-yellow: #ffe01a;
    --text-white: #ffffff;
    --text-dark: #111111;
  }
  * { margin: 0; padding: 0; box-sizing: border-box; }
  html, body { width: 1021px; height: 1200px; overflow: hidden; }
  body {
    background: var(--backdrop);
    font-family: "Saira", sans-serif;
    position: relative;
  }
  .label {
    position: absolute;
    left: 71px; top: 26px;
    width: 878px; height: 1148px;
    background: var(--label-black);
    overflow: hidden;
  }
  .label > * { position: absolute; }
  .band {
    left: 0; width: 100%; height: 58px;
    background:
      linear-gradient(to bottom,
        var(--label-black) 0 8px,
        var(--band-deep) 8px 12px,
        var(--band-cyan) 12px 26px,
        var(--band-blue) 26px 38px,
        var(--label-black) 38px 46px,
        var(--band-blue) 46px 50px,
        var(--label-black) 50px 100%);
  }
  .band--top { top: 20px; }
  .band--bottom { top: 1062px; transform: scaleY(-1); }
  .brand {
    top: 130px; left: 0; width: 100%;
    display: flex; justify-content: center; align-items: center; gap: 14px;
    color: var(--brand-green);
    font-size: 58px; font-weight: 400; line-height: 1;
  }
  .brand-dot {
    width: 30px; height: 30px; border-radius: 50%;
    background: var(--brand-green);
  }
  .grade {
    top: 248px; left: 0; width: 100%;
    text-align: center; color: var(--text-white);
    font-size: 80px; font-weight: 500; line-height: 1;
  }
  .product-name {
    top: 349px; left: 117px; width: 671px; height: 103px;
    background: linear-gradient(to right, var(--band-cyan), var(--band-blue) 60%, var(--band-deep));
    border-radius: 14px;
    color: var(--text-white);
    font-size: 96px; font-weight: 600; line-height: 103px;
    text-align: center;
  }
  .spectrum {
    top: 490px; left: 241px; width: 423px; height: 68px;
    background: var(--chip-green);
    color: var(--text-dark);
    font-size: 52px; font-weight: 500; line-height: 68px;
    text-align: center;
  }
  .strength {
    top: 570px; left: 0; width: 100%;
    text-align: center; color: var(--chip-green);
    font-size: 40px; font-weight: 400; line-height: 1.2;
  }
  .flavor {
    top: 653px; left: 0; width: 100%; height: 74px;
    display: flex; justify-content: center;
  }
  .flavor svg { position: absolute; left: 216px; top: 0; }
  .flavor span {
    position: relative;
    color: var(--text-dark);
    font-size: 54px; font-weight: 500; line-height: 74px;
  }
  .benefits { top: 757px; left: 216px; list-style: none; }
  .benefit {
    position: relative; height: 66px; margin-bottom: 17px;
    display: flex; align-items: center;
  }
  .benefit-bar {
    position: absolute; left: 20px; top: 2px; height: 62px;
    background: linear-gradient(to right, var(--band-deep), var(--band-blue));
    clip-path: polygon(0 0, 100% 0, calc(100% - 40px) 100%, 0 100%);
  }
  .benefit:nth-child(1) .benefit-bar { width: 453px; }
  .benefit:nth-child(2) .benefit-bar { width: 408px; }
  .benefit:nth-child(3) .benefit-bar { width: 363px; }
  .benefit-icon { position: relative; width: 66px; height: 66px; }
  .benefit-text {
    position: relative; margin-left: 22px;
    color: var(--text-white);
    font-size: 40px; font-weight: 400;
  }
  .net-volume {
    top: 1019px; left: 22px; width: 266px; height: 57px;
    background: var(--band-blue);
    color: var(--text-white);
    font-size: 34px; font-weight: 400; line-height: 57px;
    padding-left: 16px;
  }
</style>
</head>
<body>
  <main class="label">
    <div class="band band--top"></div>

    <div class="brand"><span class="brand-dot"></span><span class="brand-name">Vel OrtaWorks</span></div>
    <h1 class="grade">Premium</h1>
    <h2 class="product-name">Hemp Extract</h2>
    <p class="spectrum">Full Spectrum</p>
    <p class="strength">1,200mg</p>

    <div class="flavor">
      <svg width="462" height="74" viewBox="0 0 462 74">
        <path d="M10 6 L452 2 L440 16 L460 22 L446 36 L458 48 L442 58 L454 72 L14 70 L26 58 L4 50 L20 38 L2 26 L18 16 Z" fill="var(--zest-yellow)"/>
      </svg>
      <span>lemon zest</span>
    </div>

    <ul class="benefits">
      <li class="benefit">
        <span class="benefit-bar"></span>
        <svg class="benefit-icon" viewBox="0 0 66 66">
          <circle cx="33" cy="33" r="31" fill="var(--band-blue)" stroke="#fff" stroke-width="3"/>
          <path d="M18 34 C16 22 28 16 35 19 C44 16 52 24 48 33 C50 40 44 45 38 43 L36 50 L28 50 L28 44 C20 44 17 40 18 34 Z" fill="#fff"/>
        </svg>
        <span class="benefit-text">balanced mind</span>
      </li>
      <li class="benefit">
        <span class="benefit-bar"></span>
        <svg class="benefit-icon" viewBox="0 0 66 66">
          <circle cx="33" cy="33" r="31" fill="var(--band-blue)" stroke="#fff" stroke-width="3"/>
          <circle cx="33" cy="17" r="7" fill="#fff"/>
          <path d="M20 27 H46 L48 46 H42 V56 H24 V46 H18 Z" fill="#fff"/>
        </svg>
        <span class="benefit-text">balanced body</span>
      </li>
      <li class="benefit">
        <span class="benefit-bar"></span>
        <svg class="benefit-icon" viewBox="0 0 66 66">
          <circle cx="33" cy="33" r="31" fill="var(--band-blue)" stroke="#fff" stroke-width="3"/>
          <circle cx="33" cy="18" r="6" fill="#fff"/>
          <path d="M27 26 H39 L40 40 L50 46 L46 50 L33 46 L20 50 L16 46 L26 40 Z" fill="#fff"/>
        </svg>
        <span class="benefit-text">balanced life</span>
      </li>
    </ul>

    <p class="net-volume">0.5 fl oz 15ml</p>

    <div class="band band--bottom"></div>
  </main>
</body>
</html>
```